Selling my Home Flyer

I need a flyer/brochure for a house listing I am putting together. I will put all of the information together for you to include in the flyer. This will only be a front and back flyer. No extra pages and no staples will be seen. This will be printed by a large office copier, not a professional copier on standard paper. Therefore no crazy dark backgrounds with lots of bleeding colors. Pictures that I want need for sure in there are Aerial with outline, Front from left, and one of the ones showing the large yard. I included a couple sample designs that I don't hate. But feel free to get creative. I will need this on a quick turnaround and I will make comments quickly as well, so submit ASAP.

Target Market(s)

People that will by my house.

Industry/Entity Type

Real Estate Agent

Font styles to use
Serif
Sans Serif

Colors

Designer to choose colors to be used in the design.

Requirements
Must have
• The pictures I mentioned above. And the price and SF and address! I forgot to tell you the address. It is 4817 Heron Lane, Palm Beach Gardens, FL 58127.
Should not have
• Anarchy. I don't want it to look too crazy. Should be pretty straight forward.

```html
<!DOCTYPE html>
<html lang="en">
<head>
<meta charset="utf-8">
<title>Pool Home Listing Flyer</title>
<link href="https://fonts.googleapis.com/css2?family=Oswald:wght@500;700&family=Montserrat:wght@400;500;600&family=Lato:wght@400;700&display=swap" rel="stylesheet">
<style>
  :root {
    --backdrop: #e6e4e1;
    --paper: #ffffff;
    --tan: #d4bfa4;
    --ink: #141414;
    --ink-soft: #2b2b2b;
  }
  * { box-sizing: border-box; margin: 0; padding: 0; }
  html, body { width: 792px; height: 1200px; overflow: hidden; background: var(--backdrop); }
  .canvas { position: relative; width: 792px; height: 1200px; }
  .page {
    position: absolute; left: 176px; width: 440px; height: 570px;
    background: var(--paper); overflow: hidden;
    box-shadow: 0 6px 18px rgba(0,0,0,.18);
    font-family: "Montserrat", sans-serif; color: var(--ink);
  }
  .page--front { top: 20px; }
  .page--back { top: 610px; }
  .photo { position: absolute; }
  .contact-band {
    position: absolute; left: 0; right: 0; bottom: 0; height: 118px; background: var(--tan);
  }
  .agent { position: absolute; left: 20px; bottom: 16px; }
  .agent-name { font-weight: 600; font-size: 12px; }
  .agent-phone { font-size: 17px; font-weight: 500; letter-spacing: .5px; margin-top: 2px; }
  .address {
    position: absolute; left: 194px; bottom: 18px; width: 126px;
    border-left: 1px solid var(--ink-soft); padding-left: 8px;
    font-size: 9px; line-height: 1.3;
  }
  .address svg { display: block; margin: 0 auto 2px; }
  .reach {
    position: absolute; right: 10px; bottom: 30px; width: 116px;
    border-left: 1px solid var(--ink-soft); padding-left: 8px;
  }
  .reach-title { font-size: 12px; font-weight: 500; }
  .reach-email { font-size: 8px; margin-top: 2px; }

  /* front */
  .logo-space {
    position: absolute; left: 222px; top: 16px; width: 168px; height: 40px;
    background: var(--tan); display: flex; align-items: center; justify-content: center;
    font-family: "Oswald", sans-serif; font-weight: 700; font-size: 20px;
  }
  .headline { position: absolute; left: 208px; top: 66px; font-family: "Oswald", sans-serif; }
  .headline-main { font-weight: 700; font-size: 44px; line-height: 1; letter-spacing: -.5px; }
  .headline-sub { font-family: "Montserrat", sans-serif; font-weight: 500; font-size: 11px; margin-top: 2px; }
  .headline-tag { font-weight: 700; font-size: 19px; line-height: 1.1; }
  .price { position: absolute; left: 26px; top: 232px; }
  .price-label { font-size: 15px; font-weight: 500; letter-spacing: .5px; }
  .price-value { font-size: 30px; font-weight: 500; letter-spacing: 1px; }
  .features { position: absolute; left: 318px; top: 300px; }
  .features-title { font-family: "Oswald", sans-serif; font-weight: 700; font-size: 22px; }
  .features-list { list-style: none; font-size: 13px; line-height: 1.7; margin-top: 2px; }

  /* back */
  .bullets {
    position: absolute; list-style: none;
    font-family: "Lato", sans-serif; font-size: 9px; line-height: 1.35;
  }
  .bullets li { position: relative; padding-left: 10px; margin-bottom: 4px; }
  .bullets li::before {
    content: ""; position: absolute; left: 1px; top: 4px;
    width: 4px; height: 4px; border-radius: 50%; background: var(--ink);
  }
  .bullets--left { left: 12px; top: 244px; width: 242px; }
  .bullets--right { left: 262px; top: 306px; width: 172px; }
  .bullets--right li { margin-bottom: 2px; }
</style>
</head>
<body>
<main class="canvas">

  <section class="page page--front" aria-label="Flyer front">
    <div class="contact-band"></div>
    <div class="photo" role="img" aria-label="Aerial photo of the home with tile roof and surrounding trees" style="left:0;top:0;width:196px;height:218px;background:linear-gradient(160deg,#5d7a4a,#9a8670 55%,#4e6b3c);"></div>
    <div class="logo-space">LOGO SPACE</div>
    <div class="headline">
      <div class="headline-main">POOL HOME</div>
      <div class="headline-sub">ON COVETED CORNER LOT</div>
      <div class="headline-tag">WITH OVERSIZED YARD</div>
    </div>
    <div class="photo" role="img" aria-label="Bright interior entry hall with light walls" style="left:206px;top:152px;width:234px;height:130px;background:linear-gradient(135deg,#cfc7b6,#eeeae2 55%,#a99a86);"></div>
    <div class="price">
      <div class="price-label">OFFERED AT</div>
      <div class="price-value">$570,000</div>
    </div>
    <div class="photo" role="img" aria-label="Large green yard in front of the two-story home under palm trees" style="left:62px;top:306px;width:252px;height:168px;background:linear-gradient(180deg,#9fc0dc,#6c8f58 45%,#4f8a2e);"></div>
    <div class="features">
      <div class="features-title">FEATURES</div>
      <ul class="features-list">
        <li>SIZE– 2,307 SF</li>
        <li>3 BEDROOMS</li>
        <li>2 ½ BATHROOMS</li>
      </ul>
    </div>
    <div class="agent">
      <div class="agent-name">Dana Merrow</div>
      <div class="agent-phone">555-014-2287</div>
    </div>
    <div class="address">
      <svg width="8" height="11" viewBox="0 0 8 11"><path d="M4 0a4 4 0 0 0-4 4c0 3 4 7 4 7s4-4 4-7a4 4 0 0 0-4-4z" fill="#141414"/><circle cx="4" cy="4" r="1.4" fill="#d4bfa4"/></svg>
      4817 Heron Lane, Palm Beach Gardens, FL 58127.
    </div>
    <div class="reach">
      <div class="reach-title">Get In Touch</div>
      <div class="reach-email">dana@larkwoodhomes.com</div>
    </div>
  </section>

  <section class="page page--back" aria-label="Flyer back">
    <div class="contact-band"></div>
    <div class="photo" role="img" aria-label="Screened pool with turquoise water at dusk" style="left:0;top:0;width:220px;height:236px;background:linear-gradient(180deg,#c9b9a6,#8a8c8e 45%,#1aa3b5 70%,#0f6f82);"></div>
    <div class="photo" role="img" aria-label="Bedroom with ceiling fan and exercise bike" style="left:200px;top:0;width:240px;height:96px;background:linear-gradient(135deg,#ddd6ca,#b8ae9e);"></div>
    <div class="photo" role="img" aria-label="Open kitchen with white cabinets and island" style="left:232px;top:102px;width:208px;height:96px;background:linear-gradient(135deg,#e6e2dc,#a9a399 60%,#6f6a62);"></div>
    <div class="photo" role="img" aria-label="Dining room with chandelier and windows to the pool" style="left:270px;top:204px;width:170px;height:96px;background:linear-gradient(135deg,#cfc4b2,#8f7b64 60%,#e8e4dc);"></div>
    <ul class="bullets bullets--left">
      <li>This impressive home boasts one of the largest yards in Palm Beach Gardens' most family friendly community, Willowmere.</li>
      <li>Enjoy the ultimate Florida lifestyle with a beautiful pool &amp; expanded patio areas perfect for entertaining.</li>
      <li>Upgraded features throughout. Custom wood and ship lap details in all bathrooms and loft.</li>
    </ul>
    <ul class="bullets bullets--right">
      <li>New dark wood laminate flooring upstairs.</li>
      <li>New high-efficiency A/C units with smart thermostats.</li>
      <li>New pool pump and new heater controlled from your phone! Crown molding throughout.</li>
      <li>Walk-in closets.</li>
      <li>Quiet &amp; private cul-de-sac.</li>
    </ul>
    <div class="photo" role="img" aria-label="Large walk-in closet with hanging clothes" style="left:0;top:360px;width:244px;height:122px;background:linear-gradient(135deg,#b9a48c,#8c6f86 50%,#d9cfc2);"></div>
    <div class="agent">
      <div class="agent-name">Dana Merrow</div>
      <div class="agent-phone">555-014-2287</div>
    </div>
    <div class="address">
      <svg width="8" height="11" viewBox="0 0 8 11"><path d="M4 0a4 4 0 0 0-4 4c0 3 4 7 4 7s4-4 4-7a4 4 0 0 0-4-4z" fill="#141414"/><circle cx="4" cy="4" r="1.4" fill="#d4bfa4"/></svg>
      4817 Heron Lane, Palm Beach Gardens, FL 58127.
    </div>
    <div class="reach">
      <div class="reach-title">Get In Touch</div>
      <div class="reach-email">dana@larkwoodhomes.com</div>
    </div>
  </section>

</main>
</body>
</html>
```